Private Equity Firm Investment Offering Pitchbook

Complete design of seven page investment teaser. Clients include high net worth, investment institutions (Harwick Tellman, TLK, etc) and public/private investment partnerships.

This book will provide these clients a first look at our firm, provide for a brief overview of investment opportunities. This is the “first impression” document, sent both through email and printed / mailed.

Industry/Entity Type

Investment

Font styles to use
Serif

Colors
3176b5
85acd3

Requirements
Must have
• Please do not use the attached presentation for creative purposes. It is being provided purely to provide content of slides. Ty
Should not have
• White background only, thank you

```html
<!DOCTYPE html>
<html lang="en">
<head>
<meta charset="utf-8">
<title>Vantara Capital Partners – Pitchbook</title>
<link href="https://fonts.googleapis.com/css2?family=Cormorant+Garamond:wght@500;600;700&family=Arimo:wght@400;700&display=swap" rel="stylesheet">
<style>
:root{
  --navy:#1d3a60;
  --blue:#3176b5;
  --sky:#85acd3;
  --mist:#eef0f3;
  --ink:#333a44;
  --rule:#c9d6e4;
  --white:#ffffff;
}
*{box-sizing:border-box;margin:0;padding:0}
html,body{width:1200px;height:1000px;overflow:hidden;background:var(--white)}
body{position:relative;font-family:"Arimo",Arial,sans-serif;color:var(--ink)}
.slide{position:absolute;width:366px;height:268px;background:var(--white);box-shadow:0 0 0 1px #e6e9ee;overflow:hidden}
.slide::before{content:"";position:absolute;left:0;top:0;right:0;height:5px;background:var(--navy);border-bottom:2px solid var(--sky)}
.slide-title{position:absolute;left:14px;top:22px;font-family:"Cormorant Garamond",Georgia,serif;font-weight:600;font-size:17px;letter-spacing:.3px;color:var(--navy)}
.brand{position:absolute;right:12px;top:14px;display:flex;flex-direction:column;align-items:center;gap:2px}
.brand-dot{width:12px;height:12px;border-radius:50%;background:var(--blue)}
.brand-name{font-family:"Arimo",Arial,sans-serif;font-weight:700;font-size:7px;letter-spacing:.8px;color:var(--navy)}
.page-no{position:absolute;right:12px;bottom:8px;font-size:5px;color:#777}
p,li{font-size:5.2px;line-height:1.4}
.hl{color:var(--blue);font-weight:700}
b{font-weight:700}

/* cover */
.cover-photo{position:absolute;left:0;top:58px;width:366px;height:210px;background:linear-gradient(110deg,#1d3a60 0%,#2f5a8c 45%,#4c79a8 75%,#6f93b8 100%)}
.cover-text{position:absolute;left:14px;top:118px;color:var(--white)}
.cover-text h2{font-family:"Cormorant Garamond",Georgia,serif;font-weight:500;font-size:16px;line-height:1.2}
.cover-rule{width:150px;height:1px;background:var(--white);margin:6px 0 7px}
.cover-text span{font-size:7.5px}

/* investor opportunity */
.intro-box{position:absolute;left:0;top:44px;width:366px;height:50px;background:var(--mist);padding:6px 14px}
.terms-band{position:absolute;left:0;top:96px;width:366px;height:14px;background:var(--blue);color:var(--white);font-size:6.5px;font-weight:700;text-align:center;line-height:14px;letter-spacing:.4px}
.terms{position:absolute;left:14px;top:116px;width:340px;list-style:none}
.terms li{display:flex;align-items:center;gap:8px;margin-bottom:6px;min-height:12px}
.num{flex:0 0 11px;height:11px;border-radius:50%;background:var(--sky);color:var(--white);font-size:5.5px;font-weight:700;text-align:center;line-height:11px}
.disclaimer{position:absolute;left:8px;top:232px;width:330px;font-size:3.2px;line-height:1.35;color:#666}

/* firm overview */
.col{position:absolute;top:46px}
.col p{margin-bottom:4px}

/* performance */
.perf-band{position:absolute;left:0;top:45px;width:366px;height:95px;background:linear-gradient(90deg,#2c6aa6,#3e82c0)}
.perf-band h3{font-weight:400;font-size:8.5px;color:var(--white);text-align:center;margin-top:14px;line-height:1.3}
.perf-row{position:absolute;left:14px;top:113px;width:340px;display:flex;justify-content:space-between}
.perf-item{width:80px;display:flex;flex-direction:column;align-items:center;text-align:center}
.icon{width:36px;height:36px;border-radius:50%;background:var(--blue);border:3px solid #dbe6f2;display:flex;align-items:center;justify-content:center}
.perf-item.mid .icon{background:var(--sky)}
.perf-item p{margin-top:12px;font-size:5.2px}

/* investment management */
.pre-box{position:absolute;left:0;top:45px;width:366px;height:68px;background:var(--blue);color:var(--white);padding:6px 14px}
.section-head{font-family:"Cormorant Garamond",Georgia,serif;font-weight:700;font-size:9px;letter-spacing:.3px}
.pre-box p{font-size:5.4px;margin-top:3px}
.post{position:absolute;left:14px;top:122px;width:180px}
.post .section-head{color:var(--blue)}
.post ul{list-style:none;margin-top:6px}
.post li{border-bottom:1px solid #e3e7ec;padding:2px 0 3px 6px;position:relative}
.post li::before{content:"•";position:absolute;left:0}
.aside{position:absolute;left:203px;top:113px;width:163px;height:155px;background:var(--mist);padding:10px 10px}
.aside p{margin-bottom:6px}

/* leadership */
.role{font-family:"Cormorant Garamond",Georgia,serif;font-weight:700;font-size:6px;color:var(--blue);letter-spacing:.3px}
.bio{margin-bottom:4px;font-size:4.6px}

/* contact */
.contact-photo{position:absolute;left:0;top:56px;width:212px;height:212px;background:linear-gradient(135deg,#cfd6dc 0%,#8c98a4 45%,#5b6670 100%)}
.contact-panel{position:absolute;left:212px;top:56px;width:154px;height:212px;background:var(--mist)}
.avatar{position:absolute;left:228px;top:87px;width:34px;height:34px;border-radius:50%;background:#c7a78b;border:3px solid var(--blue)}
.contact-card{position:absolute;left:228px;top:130px}
.contact-card h4{font-family:"Cormorant Garamond",Georgia,serif;font-weight:700;font-size:8px;color:var(--blue)}
.contact-card .title{font-size:6px;font-weight:700;margin:2px 0 5px}
.contact-card p{font-size:4.8px}
</style>
</head>
<body>

<!-- cover A -->
<section class="slide" style="left:27px;top:62px">
  <div class="slide-title" style="top:24px">VANTARA CAPITAL PARTNERS</div>
  <div class="brand"><span class="brand-dot"></span><span class="brand-name">VANTARA</span></div>
  <div class="cover-photo" role="img" aria-label="Photo of an industrial worker handling metal parts, blue tint"></div>
  <div class="cover-text">
    <h2>Private Capital Group<br>“A Partner for the Long-Term”</h2>
    <div class="cover-rule"></div>
    <span>Presenter Name</span>
  </div>
</section>

<!-- cover B -->
<section class="slide" style="left:414px;top:62px">
  <div class="slide-title" style="top:24px">VANTARA CAPITAL PARTNERS</div>
  <div class="brand"><span class="brand-dot"></span><span class="brand-name">VANTARA</span></div>
  <div class="cover-photo" role="img" aria-label="Photo of business people in a meeting, soft blue tint" style="background:linear-gradient(110deg,#2a5687 0%,#4677a8 50%,#8eaccb 100%)"></div>
  <div class="cover-text">
    <h2>Private Capital Group<br>“A Partner for the Long-Term”</h2>
    <div class="cover-rule"></div>
    <span>Presenter Name</span>
  </div>
</section>

<!-- investor opportunity -->
<section class="slide" style="left:801px;top:62px">
  <div class="slide-title" style="top:18px">INVESTOR OPPORTUNITY</div>
  <div class="brand"><span class="brand-dot"></span><span class="brand-name">VANTARA</span></div>
  <div class="intro-box">
    <p>It is our belief that industries in our area(s) of focus are well positioned within the economy creating an opportune time to launch a boutique, SEC-registered <b>$100 million PE Fund.</b> The goal is to complete the asset raise by June 30, 2019 and immediately begin allocating. The amount and structure will allow us to access a wide array of investors which in turn will yield the necessary capital required to invest into a diverse portfolio of well-managed companies with <b>long-term growth prospects</b> within our area(s) of expertise.</p>
  </div>
  <div class="terms-band">INVESTMENT TERMS</div>
  <ul class="terms">
    <li><span class="num">1</span><p>Invest along side our clients. We are committed to <b>$5 million of the $100 million Fund.</b></p></li>
    <li><span class="num">2</span><p><b>5-7 year</b> investment term with a preferred rate of <b>8%</b>.</p></li>
    <li><span class="num">3</span><p>Our fee schedule is aligned with the interests of investors. There is a <b>1% management fee and a 10% performance</b> incentive fee that will scale higher after specific investment performance hurdles have been achieved.</p></li>
    <li><span class="num">4</span><p><b>$250,000 minimum investment</b> is ideal for high net-worth individuals and smaller institutional entities.</p></li>
    <li><span class="num">5</span><p>We are dedicated to forming <b>long-term investment partner relationships.</b> Those who can introduce us to <b>$10 million AUM</b> of investment capital (individual/pooled) will be provided co-investment opportunities on a deal by deal basis for <b>25% of the $10 million AUM commitment.</b></p></li>
  </ul>
  <p class="disclaimer"><b>Disclaimer:</b> This presentation is provided for informational purposes only and is intended to assist in considering the services offered by Vantara Capital Partners, LLC. Information contained herein is confidential. It does not constitute an offer to sell or a solicitation of an offer to buy any security. Any offer will be made solely by a confidential offering memorandum. This material may not be reproduced without prior written consent. Vantara Capital Partners, LLC 2019. All Rights Reserved.</p>
  <span class="page-no">3</span>
</section>

<!-- firm overview -->
<section class="slide" style="left:27px;top:352px">
  <div class="slide-title">FIRM OVERVIEW</div>
  <div class="brand"><span class="brand-dot"></span><span class="brand-name">VANTARA</span></div>
  <div class="col" style="left:14px;width:170px">
    <p><span class="hl">Vantara Capital Partners</span> is a Chicago-based private equity firm that identifies companies with high potential for organic growth or industry consolidation in the industrial manufacturing sectors. Vantara invests in private, lower middle market companies with a minimum of $10 million in revenue, stable cash flow, and tenured management. Current investments include the following:</p>
    <p><span class="hl">Redstone Fittings, LLC</span> (“Redstone”) is the largest, US-based manufacturer of couplings, adapters, and related components used in the firefighting industry. Its products are used in critical, life-saving applications to help connect firefighting hoses to trucks and hydrants. In addition to firefighting, Redstone’s products are also used for big-water applications such as hydraulic fracturing wells, industrial fire suppression, and emergency water distribution.</p>
    <p><span class="hl">GLX Power Services, LLC</span> (“GLX”) provides components, maintenance, and repairs to gas turbines, centrifugal gas compressors, pumps, gearboxes, and generators to the energy industry. GLX specializes in overhaul and parts manufacturing of Helio, Norvent, and Kestrel gas turbines and is a certified Norvent Distributor and repair center providing the highest quality repair and expertise concerning Norvent valves.</p>
  </div>
  <div class="col" style="left:194px;width:160px">
    <p><span class="hl">Newhaven Steel Plate, LLC</span> (“NSP”) provides specialty and standard grades of stainless steel plate in some of the widest, thickest, and longest dimensions in North America. The mill portfolio includes key grades that offer significant weight savings as well as high mechanical strength for lighter and stronger stainless.</p>
    <p><span class="hl">Pinecrest Thermal</span> was founded in 1912 and has since serviced the automotive, air conditioning and refrigeration industries as a manufacturer of extruded aluminum shapes for heat transfer. Pinecrest is also a fabricator of all-aluminum and aluminum/copper heat transfer coils. A major supplier of heat transfer products to the Automotive, Aerospace, Off-road Truck, Heavy Equipment as well as residential and commercial refrigeration markets.</p>
  </div>
  <span class="page-no">4</span>
</section>

<!-- investment performance -->
<section class="slide" style="left:414px;top:352px">
  <div class="slide-title">INVESTMENT PERFORMANCE</div>
  <div class="brand"><span class="brand-dot"></span><span class="brand-name">VANTARA</span></div>
  <div class="perf-band"><h3>A sample of return characteristics of previous investments<br>include the following</h3></div>
  <div class="perf-row">
    <div class="perf-item">
      <div class="icon"><svg width="16" height="16" viewBox="0 0 16 16" fill="none" stroke="#fff" stroke-width="1.2"><rect x="3" y="2" width="9" height="12" rx="1"/><path d="M5 5h5M5 7.5h5M5 10h3"/><circle cx="12" cy="12" r="2.5" fill="#3176b5"/></svg></div>
      <p>The results shown are for informational purposes only.</p>
    </div>
    <div class="perf-item mid">
      <div class="icon"><svg width="16" height="16" viewBox="0 0 16 16" fill="none" stroke="#fff" stroke-width="1.2"><circle cx="8" cy="8" r="2.5"/><path d="M8 1v4M8 11v4M1 8h4M11 8h4M3 3l3 3M10 10l3 3M13 3l-3 3M3 13l3-3"/></svg></div>
      <p>The returns are net of fees and expenses and are self-reported.</p>
    </div>
    <div class="perf-item">
      <div class="icon"><svg width="16" height="16" viewBox="0 0 16 16" fill="none" stroke="#fff" stroke-width="1.2"><circle cx="7" cy="7" r="5"/><path d="M5 9V7M7 9V5M9 9V6M10.5 10.5L14 14"/></svg></div>
      <p>These performance results are designed to highlight the Firm’s experience in previous SPV investments but are not designed to reflect potential returns of the proposed Fund.</p>
    </div>
    <div class="perf-item">
      <div class="icon"><svg width="16" height="16" viewBox="0 0 16 16" fill="none" stroke="#fff" stroke-width="1.2"><circle cx="8" cy="9" r="5.5"/><path d="M6.5 1.5h3M8 1.5v2M8 9l2.5-2.5M12 4l1-1"/></svg></div>
      <p>In fact, hypothetical performance results have many inherent limitations.</p>
    </div>
  </div>
  <span class="page-no">5</span>
</section>

<!-- investment management -->
<section class="slide" style="left:801px;top:352px">
  <div class="slide-title">INVESTMENT MANAGEMENT</div>
  <div class="brand"><span class="brand-dot"></span><span class="brand-name">VANTARA</span></div>
  <div class="pre-box">
    <div class="section-head">PRE-INVESTMENT</div>
    <p>We conduct robust due diligence with the dual objective of ensuring that risk/reward attributes have been fully vetted and that a well-grounded executable investment thesis and business plan have been developed. We then capitalize each investment in a manner custom-designed to facilitate the execution of the investment thesis and business plan.</p>
  </div>
  <div class="post">
    <div class="section-head">POST-INVESTMENT</div>
    <p style="font-size:5.6px;margin-top:2px">During our ownership period, we work collaboratively with each management team to ensure:</p>
    <ul>
      <li>Key investment assumptions are periodically confirmed or adjusted</li>
      <li>An environment of execution and accountability exists</li>
      <li>Internal and external reporting is timely, useful, and fully transparent</li>
      <li>Human and financial capital needs are identified and adequately met</li>
      <li>All stake holder interests are properly aligned</li>
    </ul>
  </div>
  <div class="aside">
    <p>A consistent plan of communication is executed throughout the investment cycle. This ranges from monthly calls to having our operating executives on-site not only monitoring our investment but also providing day-to-day assistance in managing and growing these organizations.</p>
    <p>We will utilize all necessary resources to ensure our investors that their capital investment is well managed and monitored. As an example, we utilize an affiliated entity Vantara Consulting to assist us in this ongoing process. They are a multi-disciplined and energy-centric consulting firm specializing in marketing, business development, business improvement, engineering, facilities management, and project management.</p>
  </div>
</section>

<!-- leadership -->
<section class="slide" style="left:27px;top:652px">
  <div class="slide-title">LEADERSHIP</div>
  <div class="brand"><span class="brand-dot"></span><span class="brand-name">VANTARA</span></div>
  <div class="col" style="left:14px;top:40px;width:170px">
    <div class="role">FOUNDER + CEO</div>
    <p class="bio">R.J. Vantara is the Founder and Chief Executive Officer of Vantara Capital, LLC. Prior to founding Vantara Capital, R.J. was Chief Executive Officer of Autoframe Repair, Inc., the seventh-largest U.S.-based automotive collision repair company with centers throughout Illinois, Indiana, and Florida.</p>
    <div class="role">SENIOR MANAGING DIRECTOR</div>
    <p class="bio">Jonas Brell, CPA is a Senior Managing Director at Vantara Capital Partners, LLC. Prior to joining Vantara Capital Partners, Jonas worked at Lakeshore Trust Bank where he focused on the firm’s capital allocation and requirements. Prior to his role at Lakeshore Trust, Jonas was a senior analyst at Bayview Capital Advisors, a sub-advised mutual fund company.</p>
    <div class="role">CHIEF LEGAL COUNSEL</div>
    <p class="bio">Reid Halvorsen, JD, CPA is the Chief Legal Officer of Vantara Capital, LLC. Before becoming an attorney, Reid worked for several years as a Certified Public Accountant at a public accounting firm. Following his career in accounting, he practiced law for almost two decades at several prestigious law firms in the Chicago land area, including Marsh Bennet LLP and Carlow and Finch LLP where he was a partner in the public finance group, in private practice.</p>
    <div class="role">OPERATING EXECUTIVE</div>
    <p class="bio">Jared Colton is an Operating Executive at Vantara Capital Partners, LLC in charge of manufacturing-related investments. Jared has 30 years of quality leadership experience providing positive results in multiple business units. Most recently, Jared served as the Chief Executive Officer of Crest Coatings &amp; Logistics Management Group, LLC, which provides coatings and logistics services to Fortune 50 manufacturing companies. Prior to this, Jared was President and COO of Autoframe Repair, which became one of the largest privately held collision repair operators in the United States.</p>
  </div>
  <div style="position:absolute;left:190px;top:42px;width:1px;height:205px;background:var(--rule)"></div>
  <div class="col" style="left:197px;top:40px;width:157px">
    <div class="role">OPERATING EXECUTIVE</div>
    <p class="bio">Anton Brisk, PE is an Operating Executive at Vantara Capital Partners, LLC in charge of energy-related investments. Anton also serves as the president of Vantara Consulting, LLC, an energy-focused management consulting company with clients representing some of the largest original equipment manufacturers that provide products and services in the energy sector.</p>
    <div class="role">SENIOR ASSOCIATE</div>
    <p class="bio">Dale Engstrom is a Senior Associate at Vantara Capital Partners and is responsible for identifying and evaluating investment opportunities, executing investments and supporting portfolio company management teams. Prior to joining Vantara Capital Partners, Dale worked at Whitcomb &amp; Co. in Chicago, where he focused on mergers and acquisitions for clients in the industrial sector.</p>
    <div class="role">SENIOR ADVISOR</div>
    <p class="bio">Marcus Merrill is a Senior Advisor at Vantara Capital Partners, LLC in charge of investor client service and business development. Marcus has 25 years experience within the asset management field and has held various positions including Senior Director at a global asset management firm and Founding Partner of a managed futures CTA.</p>
  </div>
  <span class="page-no">7</span>
</section>

<!-- contact -->
<section class="slide" style="left:414px;top:652px">
  <div class="slide-title">CONTACT INFORMATION</div>
  <div class="contact-photo" role="img" aria-label="Photo of two business colleagues reviewing a tablet in a bright office"></div>
  <div class="contact-panel"></div>
  <div class="avatar" role="img" aria-label="Portrait photo of the senior advisor"></div>
  <div class="contact-card">
    <h4>MARCUS D. MERRILL</h4>
    <div class="title">Senior Advisor</div>
    <p>Vantara Capital Partners<br>410 West Harbor Street<br>Suite 2200<br>Chicago, IL 60610</p>
    <p style="margin-top:6px"><b>Email:</b> mmerrill@vantaracp.com<br><b>Tel:</b> (312) 555-0148<br><b>www.vantaracp.com</b></p>
  </div>
  <span class="page-no">8</span>
</section>

</body>
</html>
```